Texas Civic Builders Summit Needs a Flyer

One-page event graphic/flyer and header needed. Logos provided.

2023 Texas Civic Builders Summit
Bold Ventures – True Accounts, True Answers, True Wins
August 10-11, 2023
San Antonio, Texas

About the Forum:
“Capital projects are full of risk. It’s not a question of eliminating risk, it’s a question of how to clearly identify it, reduce it, change it, or battle it.”
- Denise Holmgarten, Founder, U-BraMQ; San Antonio City Architect (retired)

Real Stories, Real Solutions, Real Success: U-BraMQ’s Texas Civic Builders Summit (TCBS) is designed to help you attain project success by hearing from Public Project Owners, architects, engineers, consultants, contractors, and suppliers. We are all in this together, and U-BraMQ is the organization that champions cross-collaboration and communication for project success!

For reference in design ONLY -
Here are some topic areas that bring project risks and/or rewards and that ultimately affect the Public Project Owner’s project success:

• Project Planning
• Regional Growth Shifts
• Project Funding
• Contracting
• Governmental Regulations
• Long-term COVID Impacts
• Infrastructure and Site Design
• Safety and Security
• Sustainability and Resilience
• Construction Predictability
• Leveraging Technology
• Facility Operations

Target Market(s)

Architects, Engineers, Contractors, project owners

Industry/Entity Type

Design and Construction

Requirements
Must have
• This is for a one-page (8.5x11) event graphic/flyer only - logos are provided. U-BraMQ logo, Texas Civic Builders Summit (TCBS) logo, 2023 Texas Civic Builders Summit, date, location
Nice to have
• Graphic(s) that represent the design and construction industry and the theme of this event (title, topics covered)
Should not have
• Full project description

```html
<!DOCTYPE html>
<html lang="en">
<head>
<meta charset="utf-8">
<title>2023 Texas Civic Builders Summit – Flyer and Header</title>
<link href="https://fonts.googleapis.com/css2?family=Poppins:wght@500;600;800&display=swap" rel="stylesheet">
<style>
  :root{
    --blue:#2f4aa0;
    --green:#8cbd36;
    --white:#ffffff;
    --canvas:#f3f4f6;
    --ink:#2f4aa0;
    --place-ink:#2d3e7e;
  }
  *{margin:0;padding:0;box-sizing:border-box}
  html,body{width:1200px;height:3200px;overflow:hidden;background:var(--canvas)}
  body{position:relative;font-family:"Poppins",sans-serif;color:var(--ink)}

  .flyer,.header-banner{position:absolute;left:50px;width:1100px;background:var(--white);overflow:hidden;box-shadow:0 6px 18px rgba(0,0,0,.12)}
  .flyer{top:578px;height:1425px}
  .header-banner{top:2073px;height:550px}

  .flyer-photo{position:absolute;left:0;top:0;width:1100px;height:900px;
    background:linear-gradient(180deg,#2fb7b4 0%,#55c2b6 22%,#3a9f9c 45%,#2e8a6c 70%,#3d8f3a 100%)}
  .flyer-shapes{position:absolute;left:0;top:0;width:1100px;height:1425px}

  .event-mark{position:absolute;left:265px;top:70px;width:600px;text-align:center;
    font-weight:600;font-size:42px;line-height:1.1;color:var(--blue)}

  .centered{position:absolute;left:0;width:100%;text-align:center;line-height:1}
  .year{top:732px;font-weight:800;font-size:146px;color:var(--green);letter-spacing:-2px}
  .title{top:868px;font-weight:800;font-size:104px;line-height:.96;color:var(--blue);letter-spacing:-2px}
  .theme{top:1076px;font-weight:800;font-size:54px;color:var(--blue)}
  .theme span{color:var(--green)}
  .pillars{top:1140px;display:flex;justify-content:center;gap:34px;font-weight:500;font-size:35px;color:var(--blue)}
  .pillars li{list-style:none;display:flex;align-items:center;gap:10px;white-space:nowrap}
  .pillars svg{width:22px;height:22px}

  .when-where{display:flex;justify-content:center;align-items:center;gap:22px}
  .flyer .when-where{top:1205px}
  .date-pill{display:flex;align-items:stretch;border:3px solid var(--green);border-radius:10px;overflow:hidden;font-weight:600;line-height:1;white-space:nowrap}
  .date-pill .days{padding:6px 12px;color:var(--blue)}
  .date-pill .days sup{font-size:.55em;vertical-align:.75em}
  .date-pill .yr{background:var(--green);color:var(--white);padding:6px 12px}
  .flyer .date-pill{font-size:36px}
  .place{display:flex;align-items:center;gap:10px;font-weight:500;color:var(--place-ink);white-space:nowrap}
  .flyer .place{font-size:34px}
  .place svg{width:28px;height:32px}

  .org-mark{position:absolute;left:66px;top:1338px;display:flex;align-items:center;gap:14px;
    font-weight:500;font-size:36px;line-height:1;color:var(--blue);white-space:nowrap}
  .org-mark i{display:block;width:60px;height:60px;border-radius:50%;background:var(--blue)}
  .contact{position:absolute;left:440px;top:1348px;width:640px;display:flex;justify-content:center;gap:28px;align-items:center;
    font-weight:500;font-size:29px;line-height:1;color:var(--white);white-space:nowrap}
  .contact span{display:flex;align-items:center;gap:9px}
  .contact svg{width:20px;height:20px;flex:none}

  .banner-photo{position:absolute;left:0;top:0;width:1100px;height:550px}
  .banner-mark{position:absolute;left:35px;top:48px;width:440px;text-align:center;font-weight:600;font-size:30px;line-height:1.1;color:var(--blue)}
  .banner-copy{position:absolute;left:20px;width:440px;text-align:center;line-height:1}
  .banner-year{top:178px;font-weight:800;font-size:96px;color:var(--green);letter-spacing:-1px}
  .banner-title{top:276px;font-weight:800;font-size:45px;line-height:1.02;color:var(--blue);letter-spacing:-1px}
  .header-banner .when-where{position:absolute;left:20px;width:440px;top:400px}
  .header-banner .date-pill{font-size:30px}
  .banner-place{position:absolute;left:20px;width:440px;top:474px;justify-content:center;font-size:30px}
</style>
</head>
<body>

<section class="flyer" aria-label="Event flyer">
  <div class="flyer-photo" role="img" aria-label="Aerial city skyline with greenery and a glowing digital globe surrounded by sustainability icons"></div>

  <svg class="flyer-shapes" viewBox="0 0 1100 1425" aria-hidden="true">
    <path d="M155,0 C215,185 395,272 565,272 C735,272 915,185 975,0 Z" fill="var(--white)" stroke="var(--green)" stroke-width="6"/>
    <path d="M0,818 Q520,600 1100,790 L1100,1425 L0,1425 Z" fill="var(--blue)"/>
    <path d="M0,872 Q520,650 1100,830 L1100,1425 L0,1425 Z" fill="var(--white)"/>
    <path d="M428,1308 L1100,1308 L1100,1425 L355,1425 Q395,1320 428,1308 Z" fill="var(--blue)"/>
    <path d="M402,1312 Q365,1330 328,1425" fill="none" stroke="var(--green)" stroke-width="4"/>
  </svg>

  <div class="event-mark">Texas Civic<br>Builders Summit</div>

  <div class="centered year">2023</div>
  <h1 class="centered title">TEXAS CIVIC<br>BUILDERS SUMMIT</h1>
  <div class="centered theme">BOLD <span>VENTURES</span></div>
  <ul class="centered pillars">
    <li><svg viewBox="0 0 22 22"><circle cx="11" cy="11" r="11" fill="var(--green)"/><path d="M6 11.5l3.2 3.2L16 8" fill="none" stroke="#fff" stroke-width="2.6" stroke-linecap="round" stroke-linejoin="round"/></svg>True Accounts</li>
    <li><svg viewBox="0 0 22 22"><circle cx="11" cy="11" r="11" fill="var(--green)"/><path d="M6 11.5l3.2 3.2L16 8" fill="none" stroke="#fff" stroke-width="2.6" stroke-linecap="round" stroke-linejoin="round"/></svg>True Answers</li>
    <li><svg viewBox="0 0 22 22"><circle cx="11" cy="11" r="11" fill="var(--green)"/><path d="M6 11.5l3.2 3.2L16 8" fill="none" stroke="#fff" stroke-width="2.6" stroke-linecap="round" stroke-linejoin="round"/></svg>True Wins</li>
  </ul>

  <div class="centered when-where">
    <div class="date-pill"><span class="days">AUGUST 10<sup>TH</sup>–11<sup>TH</sup></span><span class="yr">2023</span></div>
    <div class="place"><svg viewBox="0 0 28 32"><path d="M14 3a8 8 0 0 1 8 8c0 6-8 13-8 13S6 17 6 11a8 8 0 0 1 8-8z" fill="none" stroke="var(--green)" stroke-width="2.6"/><circle cx="14" cy="11" r="3" fill="var(--green)"/><ellipse cx="14" cy="28" rx="10" ry="2.5" fill="none" stroke="var(--green)" stroke-width="2"/></svg>San Antonio, Texas</div>
  </div>

  <div class="org-mark"><i></i>U-BraMQ</div>

  <div class="contact">
    <span><svg viewBox="0 0 24 24"><path d="M6.6 10.8a15 15 0 0 0 6.6 6.6l2.2-2.2a1 1 0 0 1 1-.25 11.4 11.4 0 0 0 3.6.57 1 1 0 0 1 1 1V20a1 1 0 0 1-1 1A17 17 0 0 1 3 4a1 1 0 0 1 1-1h3.5a1 1 0 0 1 1 1c0 1.25.2 2.45.57 3.57a1 1 0 0 1-.25 1z" fill="var(--green)"/></svg>(512) 555-0184</span>
    <span><svg viewBox="0 0 24 24"><circle cx="12" cy="12" r="10" fill="none" stroke="var(--green)" stroke-width="2"/><path d="M2 12h20M12 2c3 3 3 17 0 20M12 2c-3 3-3 17 0 20" fill="none" stroke="var(--green)" stroke-width="1.6"/></svg>u-bramq.eventsite.org</span>
  </div>
</section>

<section class="header-banner" aria-label="Event header">
  <svg class="banner-photo" viewBox="0 0 1100 550">
    <defs>
      <linearGradient id="skyline" x1="0" y1="0" x2="1" y2="1">
        <stop offset="0" stop-color="#dfe6f2"/>
        <stop offset=".45" stop-color="#9fb1d6"/>
        <stop offset=".7" stop-color="#e6b98a"/>
        <stop offset="1" stop-color="#4f63a3"/>
      </linearGradient>
    </defs>
    <path d="M470,0 L1100,0 L1100,550 L470,550 L600,275 Z" fill="url(#skyline)" role="img" aria-label="Engineer holding blueprints blended with a city skyline and highway at sunrise"/>
    <path d="M428,0 L468,0 L598,275 L468,550 L428,550 L558,275 Z" fill="var(--blue)"/>
    <path d="M405,0 L535,275 L405,550" fill="none" stroke="var(--green)" stroke-width="5"/>
  </svg>

  <div class="banner-mark">Texas Civic<br>Builders Summit</div>
  <div class="banner-copy banner-year">2023</div>
  <h2 class="banner-copy banner-title">TEXAS CIVIC<br>BUILDERS SUMMIT</h2>
  <div class="when-where">
    <div class="date-pill"><span class="days">AUGUST 10<sup>TH</sup>–11<sup>TH</sup></span><span class="yr">2023</span></div>
  </div>
  <div class="place banner-place"><svg viewBox="0 0 28 32"><path d="M14 3a8 8 0 0 1 8 8c0 6-8 13-8 13S6 17 6 11a8 8 0 0 1 8-8z" fill="none" stroke="var(--green)" stroke-width="2.6"/><circle cx="14" cy="11" r="3" fill="var(--green)"/><ellipse cx="14" cy="28" rx="10" ry="2.5" fill="none" stroke="var(--green)" stroke-width="2"/></svg>San Antonio, Texas</div>
</section>

</body>
</html>
```